Insurtech company need a banner design in an exhibition

We need a poster design for event exhibition with the size of 2000mm height and 850mm width.

The feeling of the design should be peaceful, smart and secure, also relate it to the insurance industry.

Banner shouldn't be a lot of text, should be simple, clean and easy to read.

For the color theme, please follow our website: http://veltrapine.com

Our company, BrivaForge provides mobile and AI solutions for insurance companies and claims handling companies.

More detail description, you can check out our website as I mentioned above.

Example of size model 850:
http://www.quellmarkstands.com.au/images/html_zero_pix1.gif
Updates

Target Market(s)

Corporate companies, insurance companies, claims handling companies, major retailers

Industry/Entity Type

Insurance

Logo Text

Briva Forge

Font styles to use
Other font styles liked:
• Roboto or suitable font style

Requirements
Must have
• Mobile, Video lives streaming & Artificial intelligent
• Please follow the color theme of our website: http://veltrapine.com
Nice to have
• Professional and techy feeling, try to relate to insurance

```html
<!DOCTYPE html>
<html lang="en">
<head>
<meta charset="utf-8">
<title>Briva Forge – Mobile &amp; AI Solutions for Insurance</title>
<link rel="stylesheet" href="https://fonts.googleapis.com/css2?family=Oswald:wght@300;500;600&family=Roboto+Condensed:ital,wght@0,400;0,700;1,700&display=swap">
<style>
  :root {
    --stage: #ececee;
    --banner-white: #ffffff;
    --band-grey: #d5d6d9;
    --brand-blue: #3b5cae;
    --navy: #233f8d;
    --list-bg: #e3e5f3;
    --tick-red: #d9232b;
    --photo-dark: #1d2630;
    --photo-mid: #3d6f87;
    --photo-light: #8fb4c6;
  }
  * { margin: 0; padding: 0; box-sizing: border-box; }
  html, body { width: 1200px; height: 789px; overflow: hidden; }
  body {
    background: var(--stage);
    display: flex;
    align-items: center;
    justify-content: center;
  }
  .banner {
    position: relative;
    width: 340px;
    height: 750px;
    background: var(--banner-white);
    overflow: hidden;
    box-shadow: 0 4px 18px rgba(0,0,0,0.12);
  }
  .banner__shapes { position: absolute; inset: 0; }
  .logo {
    position: absolute;
    top: 18px;
    left: 0;
    width: 290px;
    display: flex;
    justify-content: center;
    align-items: center;
    gap: 8px;
  }
  .logo__dot {
    width: 16px; height: 16px; border-radius: 50%;
    background: var(--brand-blue);
  }
  .logo__name {
    font-family: 'Oswald', sans-serif;
    font-weight: 500;
    font-size: 24px;
    color: var(--brand-blue);
    letter-spacing: 0.5px;
  }
  .headline {
    position: absolute;
    top: 86px;
    left: 26px;
    right: 16px;
    font-family: 'Oswald', sans-serif;
    color: var(--brand-blue);
    text-transform: uppercase;
    line-height: 1;
  }
  .headline__light { font-weight: 300; }
  .headline__bold { font-weight: 600; }
  .headline__line1 { font-size: 40px; display: block; }
  .headline__line1 .amp { font-size: 30px; }
  .headline__line2 { font-size: 63px; display: block; margin-top: 2px; letter-spacing: 0.5px; }
  .headline__line3 { display: block; margin-top: 4px; }
  .headline__line3 .headline__light { font-size: 38px; }
  .headline__line3 .headline__bold { font-size: 44px; }
  .photo {
    position: absolute;
    top: 262px;
    left: 0;
    width: 340px;
    height: 290px;
    background:
      radial-gradient(ellipse at 75% 55%, var(--photo-light) 0%, transparent 45%),
      linear-gradient(90deg, var(--photo-mid) 0%, var(--photo-dark) 40%, var(--photo-dark) 60%, var(--photo-mid) 100%);
  }
  .benefits {
    position: absolute;
    top: 548px;
    left: 62px;
    right: 10px;
    list-style: none;
    font-family: 'Roboto Condensed', sans-serif;
    font-style: italic;
    font-weight: 700;
    font-size: 13.5px;
    color: var(--navy);
  }
  .benefits li {
    display: flex;
    align-items: center;
    gap: 8px;
    line-height: 20px;
  }
  .benefits svg { flex: none; }
  .contact-email {
    position: absolute;
    top: 680px;
    left: 62px;
    font-family: 'Oswald', sans-serif;
    font-weight: 300;
    font-size: 15px;
    color: var(--navy);
  }
  .web-bar {
    position: absolute;
    left: 0; right: 0; bottom: 0;
    height: 44px;
    background: var(--navy);
    display: flex;
    align-items: center;
    justify-content: center;
    font-family: 'Roboto Condensed', sans-serif;
    font-weight: 700;
    font-size: 20px;
    color: var(--banner-white);
  }
</style>
</head>
<body>
  <main class="banner">
    <svg class="banner__shapes" width="340" height="750" viewBox="0 0 340 750" aria-hidden="true">
      <polygon points="0,0 340,0 340,6 290,70 0,70" fill="var(--band-grey)"/>
    </svg>

    <div class="logo">
      <span class="logo__dot"></span>
      <span class="logo__name">Briva Forge</span>
    </div>

    <h1 class="headline">
      <span class="headline__line1 headline__light">Mobile <span class="amp">&amp;</span> AI</span>
      <span class="headline__line2 headline__bold">Solutions</span>
      <span class="headline__line3"><span class="headline__light">For </span><span class="headline__bold">Insurance</span></span>
    </h1>

    <div class="photo" role="img" aria-label="Businessman in a dark shirt touching floating translucent app icons for home, car, money and a family under an umbrella"></div>

    <svg class="banner__shapes" width="340" height="750" viewBox="0 0 340 750" aria-hidden="true">
      <polygon points="40,532 340,532 340,706 0,706 0,640" fill="var(--list-bg)"/>
    </svg>

    <ul class="benefits">
      <li><svg width="12" height="11" viewBox="0 0 12 11"><path d="M1 6 L4.5 9.5 L11 1" fill="none" stroke="var(--tick-red)" stroke-width="2"/></svg>Reduce claims cost</li>
      <li><svg width="12" height="11" viewBox="0 0 12 11"><path d="M1 6 L4.5 9.5 L11 1" fill="none" stroke="var(--tick-red)" stroke-width="2"/></svg>Reduce claims cycle time</li>
      <li><svg width="12" height="11" viewBox="0 0 12 11"><path d="M1 6 L4.5 9.5 L11 1" fill="none" stroke="var(--tick-red)" stroke-width="2"/></svg>Reduce fraud</li>
      <li><svg width="12" height="11" viewBox="0 0 12 11"><path d="M1 6 L4.5 9.5 L11 1" fill="none" stroke="var(--tick-red)" stroke-width="2"/></svg>Improve accuracy of claims value</li>
      <li><svg width="12" height="11" viewBox="0 0 12 11"><path d="M1 6 L4.5 9.5 L11 1" fill="none" stroke="var(--tick-red)" stroke-width="2"/></svg>Self-service &amp; automate claims processes</li>
      <li><svg width="12" height="11" viewBox="0 0 12 11"><path d="M1 6 L4.5 9.5 L11 1" fill="none" stroke="var(--tick-red)" stroke-width="2"/></svg>Claim progress tracking mechanism</li>
    </ul>

    <p class="contact-email">TEAM@VELTRAPINE.COM</p>
    <footer class="web-bar">www.veltrapine.com</footer>
  </main>
</body>
</html>
```